Kova upkeep RT Sun Systems

Solar power system install
Services and maintenance
wiring, Rewinding and Renovation
Switch Board Upgrade
Power and lighting point
t doesn’t matter how much you spend on quality parts, your solar system will let you down if your design and installation are sub-par. Have your solar system tailored and installed by our Master Electrician and Bright Power Guild Accredited team.

Target Market(s)

sales and installed

Industry/Entity Type

Solar install and retailer

Contact Information for Business Card

Name , Email, Phone Number ,Business address,

Font styles to use
Serif

Colors
0054AA
0677BA
7BADD7
CADEEF
E8F1F8

Requirements
Must have
• clear and bright
Nice to have
• new design
Should not have
• unclear pictures

```html
<!DOCTYPE html>
<html lang="en">
<head>
<meta charset="utf-8">
<title>Kova upkeep – Business Card</title>
<link href="https://fonts.googleapis.com/css2?family=Roboto:wght@400;500&display=swap" rel="stylesheet">
<style>
  :root {
    --page-bg: #e6e9ed;
    --blue-deep: #0054AA;
    --blue-mid: #0677BA;
    --blue-soft: #7BADD7;
    --blue-pale: #CADEEF;
    --card-light: #E8F1F8;
    --green: #3f9a2f;
    --green-light: #7dc142;
    --white: #ffffff;
  }
  html, body {
    margin: 0;
    padding: 0;
    width: 1200px;
    height: 1054px;
    overflow: hidden;
    background: var(--page-bg);
    font-family: "Roboto", Arial, sans-serif;
  }
  .card {
    position: absolute;
    left: 100px;
    top: 224px;
    width: 1000px;
    height: 606px;
    border-radius: 24px;
    overflow: hidden;
    background: var(--card-light);
    box-shadow: 0 10px 30px rgba(0, 40, 90, 0.18);
  }
  .card-shapes {
    position: absolute;
    inset: 0;
  }
  .holder {
    position: absolute;
    left: 70px;
    top: 110px;
    color: var(--white);
  }
  .holder-name {
    margin: 0;
    font-size: 37px;
    font-weight: 500;
    color: var(--green-light);
    letter-spacing: 0.2px;
  }
  .holder-role {
    margin: 6px 0 0;
    font-size: 25px;
    font-weight: 400;
  }
  .address {
    position: absolute;
    left: 70px;
    top: 286px;
    margin: 0;
    font-style: normal;
    font-size: 25px;
    line-height: 38px;
    color: var(--white);
  }
  .contact-list {
    position: absolute;
    left: 70px;
    top: 374px;
    margin: 0;
    padding: 0;
    list-style: none;
    font-size: 25px;
    color: var(--white);
  }
  .contact-list li {
    display: flex;
    align-items: center;
    height: 38px;
  }
  .contact-icon {
    width: 22px;
    height: 22px;
    margin-right: 28px;
    fill: var(--green-light);
  }
  .brand {
    position: absolute;
    left: 580px;
    top: 120px;
    width: 380px;
    text-align: center;
  }
  .brand-dot {
    display: block;
    width: 170px;
    height: 170px;
    margin: 0 auto 44px;
    border-radius: 50%;
    background: var(--blue-pale);
  }
  .brand-name {
    margin: 0;
    font-size: 48px;
    line-height: 56px;
    font-weight: 500;
    color: var(--blue-mid);
    white-space: nowrap;
  }
</style>
</head>
<body>
  <section class="card">
    <svg class="card-shapes" viewBox="0 0 1000 606" width="1000" height="606" aria-hidden="true">
      <defs>
        <linearGradient id="blueField" x1="0" y1="0" x2="1" y2="1">
          <stop offset="0" stop-color="#0677BA"/>
          <stop offset="0.55" stop-color="#0a6ab3"/>
          <stop offset="1" stop-color="#0054AA"/>
        </linearGradient>
        <linearGradient id="lightField" x1="0" y1="0" x2="1" y2="1">
          <stop offset="0" stop-color="#ffffff"/>
          <stop offset="1" stop-color="#E8F1F8"/>
        </linearGradient>
      </defs>
      <rect width="1000" height="606" fill="url(#lightField)"/>
      <path d="M0 0 H626 C540 150 500 440 640 606 H0 Z" fill="#3f9a2f"/>
      <path d="M0 0 H626 C540 150 496 420 590 606 H0 Z" fill="url(#blueField)"/>
    </svg>

    <header class="holder">
      <h1 class="holder-name">Mara Lin Ortez</h1>
      <p class="holder-role">Managing Director</p>
    </header>

    <address class="address">58 Harbor Lane, Westmoor,<br>Fairvale, US 204718</address>

    <ul class="contact-list">
      <li>
        <svg class="contact-icon" viewBox="0 0 24 24" aria-hidden="true"><path d="M4 4h5l2 5-3 2a11 11 0 0 0 5 5l2-3 5 2v5a2 2 0 0 1-2 2A17 17 0 0 1 2 6a2 2 0 0 1 2-2z"/></svg>
        555-014-2290
      </li>
      <li>
        <svg class="contact-icon" viewBox="0 0 24 24" aria-hidden="true"><path d="M2 5h20v14H2z M3.5 6.5 12 13l8.5-6.5" stroke="#0677BA" stroke-width="1.5"/></svg>
        mara@kovaupkeep.com
      </li>
      <li>
        <svg class="contact-icon" viewBox="0 0 24 24" aria-hidden="true"><circle cx="12" cy="12" r="10"/><path d="M2 12h20M12 2c3 3 3 17 0 20M12 2c-3 3-3 17 0 20" stroke="#0677BA" stroke-width="1.3" fill="none"/></svg>
        www.kovaupkeep.com
      </li>
    </ul>

    <div class="brand">
      <span class="brand-dot" aria-hidden="true"></span>
      <p class="brand-name">Kova upkeep</p>
    </div>
  </section>
</body>
</html>
```